Rundverpackung Design
Zielgruppe
Ich bin Olivenölexperte und betreibe Handel mit handverlesenen und hochwertigen Olivenölen aus Italien, Griechenland und Spanien..sowie auch dazugehörigen anderen Produkten wie Balsmacio, Pestos etc.
Aufgabenstellung
Es geht um 2 Deisgn's!
1. Rundverpackung aus Papprollen, Papphüslen
2. Rundverpackung aus Alu
Abmessungen ~d=107mm und Höhe 337mm
Das Design sollte sich an meinem Corporate Design orientieren und sollte als Geschenks- Versandverpackung zum Einsatz kommen.
Eine Nährqertangabe sowie auch Barcode, QR Code sind nicht notwendig.
Es sollte eine ansprechende Geschenkeverpackung sein, orientierend an einige Vorlagen in dwn Dateien.

```html
<!DOCTYPE html>
<html lang="de">
<head>
<meta charset="utf-8">
<title>Rundverpackung – Olivenhain Serra</title>
<link rel="stylesheet" href="https://fonts.googleapis.com/css2?family=Noto+Serif:wght@400;700&family=Roboto:ital,wght@1,700&display=swap">
<style>
  :root {
    --gold-dark: #858300;
    --gold-mid: #9a9808;
    --gold-light: #a6a412;
    --aubergine: #2f0f33;
    --olive-ink: #4a4502;
    --band-ink: #3d3a05;
  }
  html, body {
    margin: 0;
    padding: 0;
    overflow: hidden;
    background: #ffffff;
  }
  .package-wrap {
    position: relative;
    width: 1200px;
    height: 1200px;
    overflow: hidden;
    background: var(--aubergine);
  }
  .brushed-metal {
    position: absolute;
    left: 0;
    width: 1200px;
    background:
      repeating-linear-gradient(90deg, rgba(255,255,255,0.05) 0 1px, rgba(0,0,0,0.04) 1px 3px, rgba(255,255,255,0.02) 3px 5px),
      linear-gradient(180deg, var(--gold-dark) 0%, var(--gold-mid) 55%, var(--gold-light) 100%);
  }
  .metal-top { top: 0; height: 1049px; }
  .metal-band { top: 1049px; height: 54px; }
  .wave-shape {
    position: absolute;
    left: 0;
    top: 0;
    width: 1200px;
    height: 1200px;
  }
  .band-text {
    position: absolute;
    top: 1049px;
    left: 0;
    width: 1200px;
    height: 54px;
    line-height: 54px;
    margin: 0;
    text-align: center;
    font-family: "Roboto", Arial, sans-serif;
    font-style: italic;
    font-weight: 700;
    font-size: 29px;
    color: var(--band-ink);
  }
  .brand-emblem {
    position: absolute;
    left: 412px;
    top: 428px;
    width: 376px;
    height: 376px;
    box-sizing: border-box;
    border: 14px solid var(--olive-ink);
    border-radius: 50%;
    display: flex;
    align-items: center;
    justify-content: center;
    text-align: center;
    font-family: "Noto Serif", Georgia, serif;
    font-weight: 700;
    font-size: 48px;
    line-height: 1.15;
    color: var(--olive-ink);
  }
  .brand-mini {
    position: absolute;
    left: 1069px;
    top: 921px;
    width: 112px;
    height: 112px;
    box-sizing: border-box;
    border: 4px solid var(--gold-light);
    border-radius: 50%;
    display: flex;
    align-items: center;
    justify-content: center;
    text-align: center;
    font-family: "Noto Serif", Georgia, serif;
    font-weight: 700;
    font-size: 15px;
    line-height: 1.15;
    color: var(--gold-light);
  }
  .orientation-arrow {
    position: absolute;
    left: 25px;
    top: 427px;
    width: 70px;
    height: 95px;
  }
</style>
</head>
<body>
  <div class="package-wrap">
    <div class="brushed-metal metal-top"></div>

    <svg class="wave-shape" viewBox="0 0 1200 1200" aria-hidden="true">
      <path fill="var(--aubergine)" d="M0,352 C120,340 200,430 280,565 C380,740 470,949 600,949 C730,949 820,740 920,565 C1000,430 1080,340 1200,352 L1200,1200 L0,1200 Z"/>
    </svg>

    <svg class="orientation-arrow" viewBox="0 0 70 95" aria-label="Diese Seite nach oben">
      <polygon fill="var(--gold-light)" points="35,0 70,44 47,44 47,95 23,95 23,44 0,44"/>
    </svg>

    <div class="brand-emblem">Olivenhain<br>Serra</div>

    <div class="brushed-metal metal-band"></div>
    <p class="band-text">Speziell für Sie</p>

    <div class="brand-mini">Olivenhain<br>Serra</div>
  </div>
</body>
</html>
```